Dalwick Self Storage Billboard

This is a 12'x24' billboard. I need this billboard to scream that it is for self storage with part of or all of the billboard having a picture of a storage unit or storage units in the background that matches my logo colors. You can use a stock image for this or I attached a picture if you would want to use that. I also need the billboard to include my logo which I have attached, the phone number of 555-014-2736, and I would like the billboard to say the following:
-Rent 100% Online at DalwickSelfStorage.example (emphasize this)
-Drive-Up & Temp-Controlled Units
-Covered & Uncovered Boat/RV Parking

I would also like there to be an arrow pointing LEFT on the bottom of the billboard that says: Millbrook Landing Apartments | 555-014-2981

```html
<!DOCTYPE html>
<html lang="en">
<head>
<meta charset="utf-8">
<title>Dalwick Self Storage Billboard</title>
<link href="https://fonts.googleapis.com/css2?family=Bebas+Neue&family=Oswald:wght@500;600&family=Poppins:wght@500;700;800&display=swap" rel="stylesheet">
<style>
  :root {
    --brand-blue: #0a56a6;
    --deep-blue: #0b3f7e;
    --navy: #0b1c33;
    --band: #262626;
    --ink: #222222;
    --tick: #7a7a7a;
    --white: #ffffff;
    --page: #e6e6e6;
  }
  * { margin: 0; padding: 0; box-sizing: border-box; }
  html, body { width: 933px; height: 1200px; overflow: hidden; }
  body { background: var(--page); position: relative; }

  .billboard {
    position: absolute; left: 46px; top: 390px;
    width: 840px; height: 420px;
    background: var(--white);
    box-shadow: 0 6px 24px rgba(0,0,0,.25);
    overflow: hidden;
  }
  .billboard__art { position: absolute; inset: 0; }

  .brand-mark {
    position: absolute; left: 0; width: 456px; top: 32px;
    display: flex; justify-content: center; align-items: center; gap: 8px;
    font-family: "Oswald", sans-serif; font-weight: 600; font-size: 24px;
    color: var(--brand-blue); line-height: 1; white-space: nowrap;
  }
  .brand-mark__square { width: 26px; height: 26px; background: var(--navy); }

  .headline { position: absolute; left: 0; top: 0; width: 456px; height: 240px; }
  .headline__top {
    position: absolute; left: 39px; top: 100px;
    font-family: "Bebas Neue", sans-serif; font-weight: 400; font-size: 82px;
    line-height: 70px; color: var(--brand-blue); white-space: nowrap;
  }
  .headline__bottom {
    position: absolute; left: 38px; top: 158px;
    font-family: "Poppins", sans-serif; font-weight: 800; font-size: 78px;
    line-height: 78px; color: var(--navy); letter-spacing: -1.5px; white-space: nowrap;
  }

  .online-bar {
    position: absolute; left: 42px; top: 239px; height: 25px; width: 373px;
    font-family: "Bebas Neue", sans-serif; color: var(--white); line-height: 25px;
    white-space: nowrap;
  }
  .online-bar__label { position: absolute; left: 11px; top: 1px; font-size: 21px; }
  .online-bar__url { position: absolute; right: 6px; top: 1px; font-size: 18px; }

  .features {
    position: absolute; left: 42px; top: 270px; width: 400px;
    list-style: none;
    font-family: "Poppins", sans-serif; font-weight: 500; font-size: 13.5px;
    line-height: 1.25; color: var(--ink);
  }
  .features__item { position: absolute; top: 0; display: flex; gap: 7px; align-items: flex-start; }
  .features__item--units { left: 0; width: 170px; }
  .features__item--parking { left: 170px; width: 210px; }
  .features__tick { flex: none; width: 16px; height: 16px; margin-top: 1px; }

  .route-label {
    position: absolute; top: 350px; height: 40px; line-height: 40px;
    font-family: "Bebas Neue", sans-serif; color: var(--white); white-space: nowrap;
  }
  .route-label--place { left: 76px; font-size: 24px; }
  .route-label--phone { left: 398px; font-size: 24px; }

  .main-phone {
    position: absolute; left: 566px; top: 348px; height: 44px; line-height: 44px;
    font-family: "Poppins", sans-serif; font-weight: 700; font-size: 33px;
    color: var(--white); letter-spacing: .5px; white-space: nowrap;
  }
</style>
</head>
<body>
  <main class="billboard">
    <svg class="billboard__art" width="840" height="420" viewBox="0 0 840 420">
      <defs>
        <linearGradient id="unitsPhoto" x1="0" y1="0" x2="1" y2="1">
          <stop offset="0" stop-color="#8fb4dc"/>
          <stop offset=".45" stop-color="#6b9ccf"/>
          <stop offset=".75" stop-color="#b8ad98"/>
          <stop offset="1" stop-color="#4a4f57"/>
        </linearGradient>
      </defs>
      <polyline points="746,0 453,31 453,308 746,325" fill="none" stroke="#111" stroke-width="2.5"/>
      <polygon points="465,43 840,3 840,322 465,297" fill="var(--brand-blue)"/>
      <polygon points="483,57 822,23 822,299 483,279" fill="var(--white)"/>
      <polygon class="photo" role="img" aria-label="Photo of a row of blue roll-up storage unit doors under a clear blue sky"
               points="486,60 819,27 819,296 486,276" fill="url(#unitsPhoto)"/>
      <rect x="0" y="325" width="840" height="95" fill="var(--band)"/>
      <rect x="236" y="239" width="179" height="25" fill="var(--navy)"/>
      <polygon points="42,239 220,239 232,251.5 220,264 42,264" fill="var(--brand-blue)"/>
      <polygon points="39,370 95,331 95,344 512,344 504,394 95,394 95,409" fill="var(--brand-blue)"/>
      <polygon points="388,344 512,344 504,394 388,394 370,369" fill="var(--deep-blue)"/>
      <polyline points="400,344 376,369 400,394" fill="none" stroke="var(--white)" stroke-width="2.5"/>
      <circle cx="537" cy="370" r="18" fill="var(--white)"/>
      <circle cx="537" cy="370" r="15" fill="var(--brand-blue)"/>
      <path d="M530 362 l4 -1 l2 5 l-2 2 q2 4 6 6 l2 -2 l5 2 l-1 4 q-3 2 -8 -1 q-6 -4 -9 -10 q-1 -3 1 -5z" fill="var(--white)"/>
    </svg>

    <div class="brand-mark"><span class="brand-mark__square"></span><span>Dalwick Self Storage</span></div>

    <h1 class="headline">
      <span class="headline__top">DALWICK SELF</span>
      <span class="headline__bottom">STORAGE</span>
    </h1>

    <p class="online-bar">
      <span class="online-bar__label">RENT 100% ONLINE AT</span>
      <span class="online-bar__url">DALWICKSELFSTORAGE.EXAMPLE</span>
    </p>

    <ul class="features">
      <li class="features__item features__item--units">
        <svg class="features__tick" viewBox="0 0 16 16"><circle cx="8" cy="8" r="8" fill="var(--tick)"/><path d="M4.5 8.2 7 10.5 11.5 5.8" fill="none" stroke="#fff" stroke-width="1.8"/></svg>
        <span>Drive-Up &amp; Temp<br>Controlled Units</span>
      </li>
      <li class="features__item features__item--parking">
        <svg class="features__tick" viewBox="0 0 16 16"><circle cx="8" cy="8" r="8" fill="var(--tick)"/><path d="M4.5 8.2 7 10.5 11.5 5.8" fill="none" stroke="#fff" stroke-width="1.8"/></svg>
        <span>Covered &amp; Uncovered<br>Boat/RV Parking</span>
      </li>
    </ul>

    <span class="route-label route-label--place">MILLBROOK LANDING APARTMENTS</span>
    <span class="route-label route-label--phone">555-014-2981</span>
    <span class="main-phone">555-014-2736</span>
  </main>
</body>
</html>
```